Stationery Design + Business Cards

Stationary (letterhead as A4 210x297mm and Letter 8.5"x11", preferably both master page + 2nd pages)

Also need business cards, standard size 50x88mm, can be vertical or horizontal.

You can use a front/back design for the business cards, or front only.

Looking at the uploaded file (bomvek, you already have that), I want it to use the first logo on the list (4 colors).

Alternative, try the grayscale version (second file).

I need the following information on the business card (in no particular order, let me know what you come up with): 

Firstname Lastlame 
Title 

Mobile +1 555-014-7392 

PelvaDyne, Inc. 
28405 Birchwin Ridge Pass 
Harlow, OR 46999 
Tel. +1 555-019-4461 
Fax +1 555-017-3058 

Web: www.pelvadyne.example 
Twitter: twitter/PelvaDyne or @PelvaDyne 
Facebook: facebook.com/PelvaDyne 

For letterhead, just the company name, address + phone number & fax number 

If you think the phone/fax or something else should not be on the business cards, or something could be missing, let me know.

```html
<!DOCTYPE html>
<html lang="en">
<head>
<meta charset="utf-8">
<title>PelvaDyne Letterhead</title>
<link rel="stylesheet" href="https://fonts.googleapis.com/css2?family=Source+Sans+3:wght@400&display=swap">
<style>
  :root {
    --canvas-bg: #ffffff;
    --sheet-bg: #ffffff;
    --sheet-shadow: rgba(0, 0, 0, 0.35);
    --brand-blue: #0d4c9e;
    --brand-orange: #f47a20;
    --band-grey: #6d6e70;
    --band-text: #ffffff;
  }
  * { margin: 0; padding: 0; box-sizing: border-box; }
  html, body {
    width: 1200px;
    height: 960px;
    overflow: hidden;
    background: var(--canvas-bg);
    font-family: "Source Sans 3", "Myriad Pro", Arial, sans-serif;
  }
  .letterhead {
    position: absolute;
    left: 278px;
    top: 25px;
    width: 644px;
    height: 911px;
    background: var(--sheet-bg);
    box-shadow: 0 0 3px var(--sheet-shadow);
  }
  .brand {
    position: absolute;
    display: flex;
    align-items: center;
    color: var(--brand-blue);
    font-weight: 400;
    line-height: 1;
    white-space: nowrap;
  }
  .brand-dot {
    border-radius: 50%;
    background: var(--brand-orange);
    flex: none;
  }
  .brand--header {
    left: 43px;
    top: 64px;
    font-size: 37px;
    letter-spacing: -0.3px;
  }
  .brand--header .brand-dot {
    width: 30px;
    height: 30px;
    margin-right: 9px;
  }
  .footer-band {
    position: absolute;
    left: 44px;
    top: 847px;
    width: 490px;
    height: 31px;
    background: var(--band-grey);
    color: var(--band-text);
    font-size: 9px;
    line-height: 31px;
    padding-left: 9px;
    white-space: nowrap;
  }
  .footer-band .sep { margin: 0 4px; }
  .brand--footer {
    left: 523px;
    top: 860px;
    font-size: 14.5px;
  }
  .brand--footer .brand-dot {
    width: 12px;
    height: 12px;
    margin-right: 4px;
  }
</style>
</head>
<body>
  <main class="letterhead">
    <header class="brand brand--header">
      <span class="brand-dot"></span>
      <span class="brand-name">PelvaDyne</span>
    </header>

    <footer>
      <p class="footer-band">PelvaDyne, Inc.<span class="sep">|</span>28405 Birchwin Ridge Pass<span class="sep">|</span>Harlow, OR 46999<span class="sep">|</span>Tel. +1 555-019-4461<span class="sep">|</span>Fax +1 555-017-3058</p>
      <div class="brand brand--footer">
        <span class="brand-dot"></span>
        <span class="brand-name">PelvaDyne</span>
      </div>
    </footer>
  </main>
</body>
</html>
```